Flyer needed for Seminar

Hello,
We are looking for eye-catching, inspiring marketing material for an educational seminar. We need 4 x 6 clubcards with the following info:

CLUBCARD FRONT:

Valtren Academy Presents:

Prayer: Past The Habit
Unlock the hidden treasures of prayer
By. Shaykh Idris Kamal Al-Tarifi

Dates:Jan 23-25, 2015
Timings: Fri - 7pm - 9:30 pm; Sat/Sun - 9am - 8 pm

Location: Dallas/Plano Corvane Suites at Ridgefield Commons
4830 Mercer Lane, Plano, TX 75093

Seating is Limited. Register Today!
www.ValtrenAcademy,example

CLUBCARD BACK:
In this unique seminar, learn how to connect spiritually with your Creator through prayer. Let us teach you the hidden meanings behind salah and why it is essential to your existence. Not only will the instructor impart the skills you'll need to master khushoo but he will delve more deeply, into the inner realms and intricacies of this ibadaa. As a result, the prayer will no longer be regarded as a mechanical chore, but an intimate meeting with the Divine. Through such insight, we hope you will leave this non-fiqh seminar with an awakened and unparalleled understanding of this fundamental pillar of Islam.

www.ValtrenAcademy.example
For more info: Email - info@valtrenacademy.example; Phone - 1-877-Valtren

Reason: I really appreciate all the submissions but am looking for something more eye-catching, something that really stirs ones interest and relates to the title of the seminar. Thank you!

```html
<!DOCTYPE html>
<html lang="en">
<head>
<meta charset="utf-8">
<title>Prayer: Past The Habit – Seminar Clubcards</title>
<link rel="stylesheet" href="https://fonts.googleapis.com/css2?family=Oswald:wght@400;500;600&family=Open+Sans:wght@400;600;700&display=swap">
<style>
  :root {
    --slate: #3e4957;
    --slate-dark: #333c48;
    --orange: #e0583a;
    --cream: #efe6d2;
    --pattern-grey: #d8d9dc;
    --white: #ffffff;
    --sky: #3fa9d8;
    --page: #8c7a55;
  }
  * { margin: 0; padding: 0; box-sizing: border-box; }
  html, body { width: 1200px; height: 800px; overflow: hidden; }
  body { background: var(--page); position: relative; font-family: "Open Sans", Arial, sans-serif; }

  .card { position: absolute; width: 570px; height: 380px; overflow: hidden; box-shadow: 0 6px 18px rgba(0,0,0,.35); }
  .card-back { left: 40px; top: 50px; background: var(--slate); }
  .card-front { left: 590px; top: 370px; background: var(--slate); }
  .card svg.shapes { position: absolute; inset: 0; }

  /* back */
  .features-ribbon { position: absolute; left: 0; top: 52px; height: 24px; width: 200px; background: var(--cream);
    clip-path: polygon(0 0, 100% 0, 93% 100%, 0 100%); padding-left: 38px;
    font-family: "Oswald", Arial, sans-serif; font-size: 14px; letter-spacing: 1px; color: var(--orange); line-height: 24px; text-transform: uppercase; }
  .features-text { position: absolute; left: 38px; top: 86px; width: 252px; color: var(--white);
    font-size: 11.5px; line-height: 1.62; }
  .contact-list { position: absolute; left: 306px; top: 28px; list-style: none; }
  .contact-list li { display: flex; align-items: center; gap: 8px; height: 22px; margin-bottom: 9px; padding: 0 12px 0 8px;
    background: var(--slate); color: var(--pattern-grey); font-family: "Oswald", Arial, sans-serif; font-size: 13px; letter-spacing: .8px; text-transform: uppercase; width: max-content; }
  .register-diagonal { position: absolute; left: 392px; top: 330px; transform: rotate(-57deg); transform-origin: left top;
    color: var(--white); font-family: "Oswald", Arial, sans-serif; font-size: 15px; line-height: 1.3; letter-spacing: .5px; text-transform: uppercase; white-space: nowrap; }

  /* front */
  .front-url { position: absolute; right: 22px; top: 5px; color: var(--white); font-size: 10.5px; font-weight: 600; }
  .presenter { position: absolute; left: 255px; top: 84px; width: 150px; text-align: center;
    font-family: "Oswald", Arial, sans-serif; font-size: 13px; line-height: 1.1; letter-spacing: 1px; text-transform: uppercase; color: var(--slate); }
  .presenter .brand { color: var(--sky); display: block; }
  .seating-note { position: absolute; left: 22px; top: 163px; color: var(--white); font-size: 10.5px; font-weight: 700;
    transform: rotate(-4.5deg); transform-origin: left center; white-space: nowrap; }
  .title-tabs { position: absolute; left: 18px; top: 192px; list-style: none; }
  .title-tabs li { height: 30px; margin-bottom: 5px; padding: 0 16px 0 22px; background: var(--slate-dark);
    color: var(--cream); font-family: "Oswald", Arial, sans-serif; font-weight: 500; font-size: 22px; line-height: 30px; letter-spacing: 1.5px; text-transform: uppercase; width: max-content;
    box-shadow: 2px 2px 4px rgba(0,0,0,.4); }
  .title-tabs li:nth-child(2) { margin-left: 10px; }
  .title-tabs li:nth-child(3) { margin-left: 22px; }
  .speaker { position: absolute; left: 338px; top: 257px; color: var(--orange); font-family: "Oswald", Arial, sans-serif; font-size: 12px; line-height: 16px; letter-spacing: .5px; text-transform: uppercase; white-space: nowrap; }
  .headline { position: absolute; left: 20px; top: 304px; color: var(--white);
    font-family: "Oswald", Arial, sans-serif; font-size: 13px; line-height: 18px; letter-spacing: .5px; text-transform: uppercase; white-space: nowrap; }
  .venue { position: absolute; left: 20px; top: 326px; color: var(--white); font-family: "Oswald", Arial, sans-serif; font-size: 12px; line-height: 1.45; text-transform: uppercase; letter-spacing: .4px; white-space: nowrap; }
  .schedule { position: absolute; right: 18px; top: 324px; color: var(--white); font-family: "Oswald", Arial, sans-serif; font-size: 11px; line-height: 1.35; text-transform: uppercase; letter-spacing: .4px; white-space: nowrap; }
</style>
</head>
<body>

<section class="card card-back" aria-label="Seminar clubcard back">
  <svg class="shapes" width="570" height="380" viewBox="0 0 570 380">
    <polygon points="0,195 290,175 290,380 0,380" fill="var(--orange)"/>
    <rect x="290" y="0" width="280" height="380" fill="var(--pattern-grey)" role="img" aria-label="Light grey interlocking geometric pattern"/>
    <polygon points="570,60 570,380 300,380" fill="var(--slate)"/>
    <rect x="288" y="0" width="4" height="380" fill="var(--orange)"/>
  </svg>
  <div class="features-ribbon">Seminar Features</div>
  <p class="features-text">In this unique seminar, learn how to connect spiritually with your Creator through prayer. Let us teach you the hidden meanings behind salah and why it is essential to your existence. Not only will the instructor impart the skills you'll need to master khushoo but he will delve more deeply, into the inner realms and intricacies of this ibadaa. As a result, the prayer will no longer be regarded as a mechanical chore, but an intimate meeting with the Divine. Through such insight, we hope you will leave this non-fiqh seminar with an awakened and unparalleled understanding of this fundamental pillar of Islam.</p>
  <ul class="contact-list">
    <li><svg width="16" height="11" viewBox="0 0 16 11"><rect x="0.5" y="0.5" width="15" height="10" fill="none" stroke="currentColor"/><polyline points="0.5,0.5 8,6 15.5,0.5" fill="none" stroke="currentColor"/></svg>info@valtrenacademy.example</li>
    <li><svg width="14" height="14" viewBox="0 0 24 24"><path fill="currentColor" d="M6.6 10.8a15 15 0 0 0 6.6 6.6l2.2-2.2a1 1 0 0 1 1-.25 11.4 11.4 0 0 0 3.6.6 1 1 0 0 1 1 1V20a1 1 0 0 1-1 1A17 17 0 0 1 3 4a1 1 0 0 1 1-1h3.5a1 1 0 0 1 1 1c0 1.250.2 2.45.6 3.6a1 1 0 0 1-.25 1z"/></svg>1-877-Valtren</li>
  </ul>
  <p class="register-diagonal">Seating is limited. Register today!<br>www.ValtrenAcademy.example</p>
</section>

<section class="card card-front" aria-label="Seminar clubcard front">
  <svg class="shapes" width="570" height="380" viewBox="0 0 570 380">
    <defs>
      <radialGradient id="handsTone" cx="65%" cy="55%" r="60%">
        <stop offset="0" stop-color="#c9b8ad"/>
        <stop offset=".45" stop-color="#7d7f84"/>
        <stop offset="1" stop-color="#2f3236"/>
      </radialGradient>
    </defs>
    <rect x="0" y="0" width="570" height="380" fill="url(#handsTone)" role="img" aria-label="Photograph of open cupped hands raised in prayer"/>
    <!-- top slate band -->
    <path d="M0,0 H570 V22 C420,30 300,70 180,100 C110,118 50,126 0,128 Z" fill="var(--slate)"/>
    <!-- white swoosh -->
    <path d="M0,128 C50,126 110,118 180,100 C300,70 420,30 570,22 V36 C430,66 330,130 200,145 C120,150 50,158 0,160 Z" fill="var(--white)"/>
    <!-- slate strip under swoosh -->
    <path d="M0,160 C50,158 120,150 200,145 C330,130 430,66 570,36 V50 C430,82 330,146 200,165 C120,175 50,182 0,185 Z" fill="var(--slate)"/>
    <rect x="0" y="160" width="12" height="220" fill="var(--slate)"/>
    <!-- bottom white tab and orange band -->
    <path d="M0,294 H250 C268,268 290,254 330,254 H570 V380 H0 Z" fill="var(--white)"/>
    <path d="M0,299 H262 C280,280 300,274 340,274 H570 V380 H0 Z" fill="var(--orange)"/>
  </svg>
  <p class="front-url">www.ValtrenAcademy.example</p>
  <p class="presenter"><span class="brand">Valtren Academy</span>Presents</p>
  <p class="seating-note">Seating Is Limited. Register Today!</p>
  <ul class="title-tabs">
    <li>Prayer:</li>
    <li>Past</li>
    <li>The Habit</li>
  </ul>
  <p class="speaker">Shaykh Idris Kamal Al-Tarifi</p>
  <p class="headline">Prayer: Past The Habit — Unlock the hidden treasures of prayer</p>
  <p class="venue">Location: Dallas/Plano Corvane Suites at Ridgefield Commons<br>4830 Mercer Lane, Plano, TX 75093</p>
  <p class="schedule">Dates: Jan 23-25, 2015<br>Timings: Fri - 7pm - 9:30 pm<br>Sat/Sun - 9am - 8 pm</p>
</section>

</body>
</html>
```